Chiropractic healthcare group business card

We are a Portland Oregon based chiropractic healthcare group. Looking for a new business card design. Something cutting edge, that shows off our new logo and tag line.Use either of the attached logos.Our tag line = "Who would you be without pain?"I'm open to about anything, impress me!!
Target Market(s)
Chiropractic patients - Auto injury, back pain, sports injuries, neck , shoulder, hip, knee, ankle pain.
Industry/Entity Type
Chiropractic
Contact Information for Business Card
Dr. Bram Holtvick, D.C.
Clinic name - Fernway Chiropractic
2 clinics
location #1
20418 NW Marwick Road
Suite B
North Plains, OR 97133
Location #2
13529 SE Calloway Street
Portland OR 97236
Main phone line 971.555.0143
website : www.FernwayClinics.example
Tag line "Who would you be without pain?"
Colors
Designer to choose colors to be used in the design.
Requirements
Must have
- Use the logo colors -- Want the orange color to be a TRUE orange.
- Both clinic address
- phone number
- website
- personal email - b.holtvick@ReliefBeginsHere.example
- tag line - "Who would you be without pain?"

```html
<!DOCTYPE html>
<html lang="en">
<head>
<meta charset="utf-8">
<title>Fernway Chiropractic – Business Card</title>
<link rel="stylesheet" href="https://fonts.googleapis.com/css2?family=Source+Serif+4:wght@400;600&display=swap">
<style>
  :root {
    --backdrop: #444444;
    --coral: #e89a8c;
    --slate: #606261;
    --ink: #5f6060;
    --white: #ffffff;
  }
  * { margin: 0; padding: 0; box-sizing: border-box; }
  html, body { width: 1200px; height: 1200px; overflow: hidden; }
  body {
    background: var(--backdrop);
    font-family: "Source Serif 4", Georgia, serif;
    position: relative;
  }
  .card {
    position: absolute;
    width: 599px;
    height: 346px;
    border-radius: 50px;
    box-shadow: 0 10px 28px rgba(0,0,0,0.35);
  }
  .card--front { left: 58px; top: 169px; background: var(--coral); }
  .card--back { left: 493px; top: 660px; background: var(--slate); }

  .brand {
    position: absolute; left: 60px; top: 42px;
    display: flex; align-items: center; gap: 10px;
    color: var(--ink); font-size: 21px; font-weight: 600;
  }
  .brand__square { width: 22px; height: 22px; background: var(--ink); }

  .divider-v {
    position: absolute; left: 395px; top: 33px;
    width: 1px; height: 68px; background: var(--ink);
  }
  .clinic-label {
    position: absolute; left: 470px; top: 35px;
    font-size: 8.5px; color: var(--ink);
  }
  .clinic-name {
    position: absolute; left: 407px; top: 42px;
    font-size: 17.5px; color: var(--ink);
  }
  .doctor {
    position: absolute; left: 407px; top: 69px;
    font-size: 13.5px; font-weight: 600; color: var(--white);
  }

  .contact {
    position: absolute; left: 25px;
    display: flex; align-items: center; gap: 12px;
    color: var(--white); font-size: 13.5px;
  }
  .contact svg { width: 32px; height: 32px; flex: none; }
  .contact--phone { top: 180px; }
  .contact--email { top: 232px; }
  .contact--web { top: 281px; }

  .pin { position: absolute; }
  .pin--small { left: 342px; top: 189px; width: 30px; height: 31px; }
  .pin--large { left: 323px; top: 245px; width: 72px; height: 72px; }

  .address {
    position: absolute; color: var(--white);
    font-size: 13.5px; line-height: 17px;
  }
  .address--north { left: 403px; top: 180px; }
  .address--portland { left: 405px; top: 273px; }

  .back-name {
    position: absolute; left: 0; right: 0; top: 102px;
    text-align: center; color: var(--coral);
    font-size: 32px; font-weight: 400;
  }
  .divider-h {
    position: absolute; left: 22px; right: 24px; top: 244px; height: 1px;
    background: linear-gradient(90deg, transparent, var(--coral) 15%, var(--coral) 85%, transparent);
  }
  .tagline {
    position: absolute; left: 0; right: 0; top: 248px;
    text-align: center; color: var(--coral); font-size: 29px;
  }
</style>
</head>
<body>

<section class="card card--front">
  <div class="brand"><span class="brand__square"></span>Fernway Chiropractic</div>

  <div class="divider-v"></div>
  <p class="clinic-label">Clinic//</p>
  <p class="clinic-name">Fernway Chiropractic</p>
  <p class="doctor">Dr. Bram Holtvick, D.C.</p>

  <div class="contact contact--phone">
    <svg viewBox="0 0 32 32" fill="none" stroke="var(--ink)" stroke-width="1.6">
      <rect x="11" y="4" width="10" height="24" rx="2"/>
      <circle cx="16" cy="25" r="0.8" fill="var(--ink)"/>
      <path d="M8 11 q-3 5 0 10 M5 9 q-5 7 0 14 M24 11 q3 5 0 10 M27 9 q5 7 0 14"/>
    </svg>
    <span>971.555.0143</span>
  </div>

  <div class="contact contact--email">
    <svg viewBox="0 0 32 32" fill="none" stroke="var(--ink)" stroke-width="1.6">
      <circle cx="16" cy="16" r="14.5"/>
      <rect x="8" y="11" width="16" height="11"/>
      <path d="M8 11 l8 6 l8 -6 M8 22 l6 -5 M24 22 l-6 -5"/>
    </svg>
    <span>b.holtvick@ReliefBeginsHere.example</span>
  </div>

  <div class="contact contact--web">
    <svg viewBox="0 0 32 32" fill="none" stroke="var(--ink)" stroke-width="1.6">
      <circle cx="16" cy="16" r="14.5"/>
      <ellipse cx="16" cy="16" rx="6" ry="14.5"/>
      <path d="M1.5 16 h29 M4 9 h24 M4 23 h24 M16 1.5 v29"/>
    </svg>
    <span>www.FernwayClinics.example</span>
  </div>

  <svg class="pin pin--small" viewBox="0 0 30 31" fill="var(--ink)">
    <path d="M15 1 a8 8 0 0 1 8 8 c0 6 -8 13 -8 13 s-8 -7 -8 -13 a8 8 0 0 1 8 -8z M15 6 a3 3 0 1 0 0.01 0z" fill-rule="evenodd"/>
    <ellipse cx="15" cy="25" rx="14" ry="5" fill="none" stroke="var(--ink)" stroke-width="2"/>
    <ellipse cx="15" cy="24.5" rx="7" ry="2.3" fill="none" stroke="var(--ink)" stroke-width="1.5"/>
  </svg>

  <p class="address address--north">20418 NW Marwick Road<br>Suite B<br>North Plains, OR 97133</p>

  <svg class="pin pin--large" viewBox="0 0 72 72" fill="var(--ink)">
    <path d="M36 1 a18 18 0 0 1 18 18 c0 12 -18 32 -18 32 s-18 -20 -18 -32 a18 18 0 0 1 18 -18z M36 10 a8 8 0 1 0 0.01 0z" fill-rule="evenodd"/>
    <ellipse cx="36" cy="58" rx="33" ry="11" fill="none" stroke="var(--ink)" stroke-width="5"/>
    <ellipse cx="36" cy="55" rx="17" ry="5" fill="none" stroke="var(--ink)" stroke-width="3"/>
  </svg>

  <p class="address address--portland">13529 SE Calloway Street<br>Portland OR 97236</p>
</section>

<section class="card card--back">
  <p class="back-name">Fernway Chiropractic</p>
  <div class="divider-h"></div>
  <p class="tagline">Who would you be without pain?</p>
</section>

</body>
</html>
```